The (Private) News Sharing Report

This is a professional and academic report of 35 pages for journalists and teachers. The topic of the report is News Sharing: journalism, social networks and technology. Attached there is an example of the kind of design we are looking for: visual, fresh and modern.

Target Market(s)

Journalists, Journalism Students, Communication Researchers,

Industry/Entity Type

Media

Font styles to use
Sans Serif

Colors
3276b5
33a6d7
886aae
b868aa

Requirements
Must have
• Copyleft images, visual style
Nice to have
• There is an example attached.

```html
<!DOCTYPE html>
<html lang="en">
<head>
<meta charset="utf-8">
<title>The (Private) News Sharing Report</title>
<link href="https://fonts.googleapis.com/css2?family=Montserrat:wght@400;500;600;700&display=swap" rel="stylesheet">
<style>
:root{
  --bg:#ece9e4;
  --navy:#1b1764;
  --indigo:#2b2cc0;
  --violet:#5b1fa2;
  --purple:#886aae;
  --magenta:#b868aa;
  --sky:#33a6d7;
  --blue:#3276b5;
  --ink:#1d1d24;
  --white:#ffffff;
}
*{margin:0;padding:0;box-sizing:border-box}
html,body{width:1200px;height:1200px;overflow:hidden;background:var(--bg);font-family:'Montserrat',sans-serif}
.canvas{position:relative;width:1200px;height:1200px}
.page{position:absolute;width:429px;height:556px;overflow:hidden;background:var(--white);box-shadow:0 3px 10px rgba(0,0,0,.25)}
.page--cover{left:158px;top:26px;background:linear-gradient(160deg,#2830c6 0%,#2a22a8 45%,#5a1d9e 100%)}
.page--credits{left:622px;top:26px}
.page--intro{left:155px;top:615px}
.page--questions{left:622px;top:615px;background:var(--navy)}

/* image areas */
.cover-photo{position:absolute;left:0;top:0;width:429px;height:556px;background:radial-gradient(ellipse 62% 55% at 62% 42%,rgba(120,96,230,.85) 0%,rgba(86,58,200,.55) 45%,rgba(40,34,170,0) 100%)}
.ornament{position:absolute}
.ornament--credits{left:0;top:340px;width:429px;height:216px;background:linear-gradient(170deg,rgba(51,166,215,.06) 0%,rgba(184,104,170,.14) 100%)}
.ornament--intro{left:300px;top:0;width:129px;height:556px;background:linear-gradient(180deg,rgba(51,166,215,.05) 0%,rgba(184,104,170,.12) 52%,rgba(51,166,215,.05) 100%)}

/* cover */
.cover-title{position:absolute;left:31px;top:38px;color:var(--white);font-weight:600;font-size:24px;line-height:28px}
.cover-sub{position:absolute;left:34px;top:164px;padding-left:9px;border-left:1px solid rgba(255,255,255,.8);color:var(--white);font-size:11px;line-height:13px;width:130px}
.cover-credit{position:absolute;left:0;right:0;top:496px;text-align:center;color:var(--white);font-size:6.8px;line-height:9.4px}
.cover-year{position:absolute;left:0;right:0;top:528px;text-align:center;color:var(--white);font-size:6.8px;font-weight:700;letter-spacing:1.5px}

/* text columns */
.column{position:absolute;width:169px;font-size:5.4px;line-height:9.4px;color:var(--ink);text-align:justify}
.column p{margin-bottom:9.4px}
.rule{position:absolute;width:1px}
.page--credits .column{left:88px;top:52px}
.page--credits .rule{left:55px;top:46px;height:276px;background:#777}
.page--intro .column{left:89px;top:35px;font-size:5.6px;line-height:9.7px}
.page--intro .column p{margin-bottom:9.7px}
.page--intro .rule{left:57px;top:35px;height:496px;background:var(--magenta)}
.column .label{margin-bottom:10px}

/* questions */
.questions-lead{position:absolute;left:59px;top:72px;width:312px;color:var(--white);font-size:7.2px;line-height:12px}
.questions-photo{position:absolute;left:0;top:184px;width:429px;height:333px;background:linear-gradient(135deg,#5b22b2 0%,#4a26b8 50%,#2a2596 100%)}
.questions-title{position:absolute;left:105px;top:166px;color:var(--white);font-size:24px;font-weight:600}
.questions-intro{position:absolute;left:134px;top:210px;color:var(--white);font-size:6.6px}
.question{position:absolute;left:0;width:429px;height:36px;color:var(--white)}
.question::before{content:"";position:absolute;left:0;top:8px;width:86px;height:1px;background:rgba(255,255,255,.55)}
.question-num{position:absolute;left:104px;top:0;font-size:12px;font-weight:600}
.question-text{position:absolute;left:134px;top:-4px;width:270px;font-size:10.4px;line-height:15px;font-weight:600}
</style>
</head>
<body>
<main class="canvas">

  <section class="page page--cover">
    <div class="cover-photo" role="img" aria-label="Photo of two people looking at a smartphone and a laptop, tinted in blue and violet"></div>
    <h1 class="cover-title">The<br>(Private)<br>News Sharing<br>Report</h1>
    <p class="cover-sub">A starting guide for researchers and journalists</p>
    <p class="cover-credit">A report by Tomás Herrero-Lanza<br>Visiting Scholar at the Capital Hill University (Washington, D.C., USA) with the help of<br>Research Grants 18/19 from the Saint Isidore University (Murcia, Spain)</p>
    <p class="cover-year">2019</p>
  </section>

  <section class="page page--credits">
    <div class="ornament ornament--credits" role="img" aria-label="Decorative network of thin blue and pink lines"></div>
    <div class="rule"></div>
    <div class="column">
      <p>This is a report by Tomás Herrero-Lanza (PhD), a journalist working at the Saint Isidore University (SIU, Spain), where he is the Head of the Communication Sciences Department. This project has been supported by a research grant from SIU to do a research stay as a Visiting Scholar at the Capital Hill University (CHU), USA, and the help of professor Martin Hale at CHU.</p>
      <p>Special thanks goes to those who collaborated in the interviews: the journalists at the Global Newsroom Institute (GNI), The Capital Ledger, Meridian Media Network, Voz Nueva, The Open Records Center, Iberia Brief, Checkpoint News and Verifica. In addition, I also want to thank the whole faculty members at the School of Communication at the Capital Hill University (CHU-SOC), who always offered their collaboration.</p>
      <p>Special thanks also goes to colleagues and scholars who selflessly dedicated their time to talk and hold meetings. They shed light on many topics reflected in to go through the report in depth. They are Ruth Calder, Omar Nadeem, Elena Varga, Paula Whitcombe, Jane Ostrow, Luis Campos, Walter Brennan, and Grace Fielding.</p>
      <p>The interviews are expressions of personal opinions as journalists and they do not necessarily express the official point of view of the media where they work. Inquiries for further information about this research can be sent to t.herrero@example.com or therrero@siu.example.edu</p>
    </div>
  </section>

  <section class="page page--intro">
    <div class="ornament ornament--intro" role="img" aria-label="Decorative network of thin blue and pink lines"></div>
    <div class="rule"></div>
    <div class="column">
      <p class="label">Introduction</p>
      <p>The job of journalists is not just longer on the internet because it ends later, it is also longer because it starts before. Not only is journalism bigger on the internet because it ends later, it is also because it starts before too. On the web, on the one hand, a journalist can have a community even before having a journalistic product. On the other hand, social recommendations, incidental consumption of news and online private messages are giving a broader reach to journalism, as we know it now.</p>
      <p>As publishing is not the end of the journalistic routine, the whole process now is longer. You cannot fully understand what "news" means for people if you do not understand how and why they are sharing the news on online private platforms. Private messaging networks are adding new challenges to journalists and the media. When we are talking about online private environments, issues such as sources, fact-checking, misinformation, privacy or (fake) news are being redefined, as well as the notions of trust, community, public service and/or media literacy.</p>
      <p>In 2018 the candidate Marco Vidal was accused of running a whole fake news campaign through ChatLine with hundreds of millions of messages against his opponent. This scandal is just an example of the growing relevance of fact-checking and the need to adopt a role in media literacy skills among users of private messaging networks by the media.</p>
      <p>Many news sites added a ChatLine sharing option in their news during the last few years (Harlow, 2014) and it seems like private channels, such as this one, could become into being a "major traffic driver for news sites" (Lindqvist, A., Moreno, V., &amp; Price, T., 2015: 10). We cannot entirely know what people are doing with news in private messaging networks, but what we can see is what the media and journalists are doing with these platforms. This report is a draft of these actions.</p>
      <p>In news sharing research, a new broad theoretical foundation is needed, with quantitative studies, digital ethnographies or uses and gratifications approaches, and even combining all these theories and deriving new ones and much more, to name but a few. We utilize the results of this preliminary research to shed light on the current needs and provide insights so that journalism can be improved, and as well as the academic research of journalism can to move forward in news sharing research.</p>
    </div>
  </section>

  <section class="page page--questions">
    <p class="questions-lead">The main goal of this executive report is to help journalists and researchers to get a deeper understanding of the news sharing processes in private messaging apps, channels, and networks. Share it, but not in a private way. Make it as public as you can.</p>
    <div class="questions-photo" role="img" aria-label="Photo of hands holding a smartphone, tinted in violet and indigo"></div>
    <h2 class="questions-title">Research Questions</h2>
    <p class="questions-intro">This report is divided into the following six research questions:</p>
    <div class="question" style="top:239px"><span class="question-num">1.</span><p class="question-text">How appropriate friendly are private online messaging networks for journalism?</p></div>
    <div class="question" style="top:283px"><span class="question-num">2.</span><p class="question-text">Can private messaging be useful for building trust between the media/journalists and communities?</p></div>
    <div class="question" style="top:327px"><span class="question-num">3.</span><p class="question-text">How can journalists use private channels/platforms to be part of a community?</p></div>
    <div class="question" style="top:371px"><span class="question-num">4.</span><p class="question-text">What are the new skills that the media landscape is requiring of journalists?</p></div>
    <div class="question" style="top:415px"><span class="question-num">5.</span><p class="question-text">What do we know about the audience that is using private messaging for News Sharing?</p></div>
    <div class="question" style="top:459px"><span class="question-num">6.</span><p class="question-text">What are the best media practices with private online messaging?</p></div>
  </section>

</main>
</body>
</html>
```